we are a college and require a design of a printable graduation certificate

our courses range from certicate III to Diploma

We would a high quality design, similar to a unveristy degree, so its meaning full to the students and looks great on the wall

our college website is: www.marlowinstitute.example.au

College

• security feature like water mark or stamp

```html
<!DOCTYPE html>
<html lang="en">
<head>
<meta charset="UTF-8">
<title>Marlow Institute – Certificate of Graduation</title>
<link rel="stylesheet" href="https://fonts.googleapis.com/css2?family=UnifrakturMaguntia&family=Gentium+Book+Plus:wght@400;700&display=swap">
<style>
  :root {
    --page-bg: #efece6;
    --frame-dark: #0d2b2b;
    --frame-blush: #f7ebf5;
    --paper: #ffffff;
    --paper-edge: #cfc8cf;
    --band-blue: #0a35ff;
    --band-cyan: #7ff8ff;
    --text-grey: #6c6c6c;
    --text-ink: #0c2f2f;
    --watermark: rgba(60, 90, 200, 0.08);
    --seal-red: #c8101a;
    --seal-soft: #e8a0a4;
  }
  * { margin: 0; padding: 0; box-sizing: border-box; }
  html, body { width: 1200px; height: 1000px; overflow: hidden; }
  body { background: var(--page-bg); position: relative; font-family: "Gentium Book Plus", Georgia, serif; }

  .certificate {
    position: absolute; left: 302px; top: 82px; width: 627px; height: 815px;
    background: var(--frame-dark);
  }
  .certificate__mat {
    position: absolute; left: 9px; top: 9px; right: 11px; bottom: 7px;
    background: var(--frame-blush); border-radius: 10px;
  }
  .certificate__paper {
    position: absolute; left: 20px; top: 18px; width: 586px; height: 782px;
    background: var(--paper); border: 1px solid var(--paper-edge); overflow: hidden;
  }
  .band-blue { position: absolute; left: 0; top: 0; width: 32px; height: 100%; background: var(--band-blue); }
  .band-cyan { position: absolute; left: 32px; top: 0; width: 17px; height: 498px; background: var(--band-cyan); }

  .centered { position: absolute; left: 49px; right: 0; text-align: center; }

  .brand { top: 52px; display: flex; flex-direction: column; align-items: center; gap: 8px; }
  .brand__mark { width: 34px; height: 34px; background: var(--band-blue); }
  .brand__name { font-size: 12px; font-weight: 700; color: var(--text-ink); letter-spacing: 0.5px; }

  .title {
    top: 140px; font-family: "UnifrakturMaguntia", serif; font-size: 47px; font-weight: 400;
    color: var(--text-grey); letter-spacing: 1px;
  }

  .watermark {
    top: 322px; display: flex; flex-direction: column; align-items: center; gap: 8px;
    pointer-events: none;
  }
  .watermark__mark { width: 230px; height: 230px; border-radius: 50%; background: var(--watermark); }
  .watermark__name { font-size: 40px; font-weight: 700; color: var(--watermark); letter-spacing: 1px; }

  .line { font-size: 22px; color: var(--text-grey); }
  .line--certify { top: 233px; }
  .line--name { top: 290px; color: var(--text-ink); }
  .line--course { top: 356px; }
  .line--program { top: 410px; }
  .line--on { top: 464px; }
  .line--year { top: 518px; }

  .fill { display: inline-block; padding-bottom: 2px; border-bottom: 2px dashed var(--text-grey); }
  .fill--name { border-color: var(--text-ink); }
  .star { font-size: 26px; color: var(--text-grey); margin: 0 6px; vertical-align: -2px; }

  .seal {
    position: absolute; left: 271px; top: 611px; width: 103px; height: 152px;
    border-radius: 50px 50px 8px 8px;
    background: linear-gradient(180deg, var(--seal-red) 0%, var(--seal-soft) 100%);
  }

  .sign { position: absolute; top: 710px; width: 100px; font-size: 24px; color: var(--text-ink); text-align: center; }
  .sign__rule { display: block; width: 100px; border-top: 2px dashed var(--text-ink); margin-bottom: 8px; }
  .sign--signature { left: 78px; }
  .sign--date { left: 444px; }
</style>
</head>
<body>
  <div class="certificate">
    <div class="certificate__mat"></div>
    <div class="certificate__paper">
      <div class="band-blue"></div>
      <div class="band-cyan"></div>

      <div class="centered watermark" aria-hidden="true">
        <div class="watermark__mark"></div>
        <div class="watermark__name">MARLOW INSTITUTE</div>
      </div>

      <div class="centered brand">
        <div class="brand__mark"></div>
        <div class="brand__name">MARLOW INSTITUTE</div>
      </div>

      <h1 class="centered title">Certificate of Graduation</h1>

      <p class="centered line line--certify">This is to certify that</p>
      <p class="centered line line--name"><span class="star">✻</span><span class="fill fill--name">student’s name</span><span class="star">✻</span></p>
      <p class="centered line line--course">has completed a course of study in</p>
      <p class="centered line line--program"><span class="fill">name of the certificate</span></p>
      <p class="centered line line--on">on</p>
      <p class="centered line line--year"><span class="fill">&nbsp;&nbsp;&nbsp;&nbsp;year&nbsp;&nbsp;&nbsp;&nbsp;</span></p>

      <div class="seal" role="img" aria-label="Red ribbon rosette seal illustration"></div>

      <div class="sign sign--signature"><span class="sign__rule"></span>Signature</div>
      <div class="sign sign--date"><span class="sign__rule"></span>Date</div>
    </div>
  </div>
</body>
</html>
```